Edgy Fun BBQ sauce label Needed

We are looking for a new label design as we are going to start to sell our competition bbq sauce. We have had multiple 1st place wins using this sauce in NPGA BBQ competitions

The Sauce name is Drizzle Away! The sauce will be bottled in mason jars, I would like the label to play off bbq themes and "sweet heat"

The sauce will be bottled in standard mason jar 16 oz and the label size is (2.3125in” x 9.4375in ) the front logo needs to fit with in (2.3125 tall x 5in across) Since the back will have to have the food label info.

We are looking for a new label design as we are going to start to sell our competition bbq sauce. We have had multiple 1st place wins using this sauce in NPGA BBQ competitions so I would like to have award winning ribbon somewhere on the label.

We have a logo for our BBQ team this can be incorporated but it is not required. If it is incorporated to the design. it does not have to be the focal point.

We are looking for this label to stand out and grab their attention we like to have fun and push the envelope a bit so don't be timid with the design.

Sauce Description: The award winning Dust Off! BBQ team has been bringing our local flavor to the BBQ competition circuit and now we are bringing it straight to your kitchen. Slather Sweat heat on any meat.

Here are some examples of sauces that are popular in competition bbq.

http://hickoryvaultgrill.example/

https://www.tallcedargrills.example/store/bbq-sauce/amber-goat-classic-barbecue-sauce

https://www.tallcedargrills.example/store/bbq-sauce/fieldhands-tangy-250
Updates

I would like to see on the label  in a the sauce name "Drizzle Away!"  then in smaller front "Barbecue Sauce"  - Then optional in yet smaller front "A Sweet Heat Treat" or " A Sweet Heat Treat for any Meat"

With all this I understand the Dust Off logo may not fit which is ok and it does not need to be on the label.

Reason: I know a bunch of Designers had just started to work on this project so I extended the deadline..

Target Market(s)

We are going to focus on catering, farmers markets, fairs, and BBQ competitions

Industry/Entity Type

Store

Font styles to use
Other font styles liked:
• Desdemona

Colors
eb1f27
f37022
fcf9ce
fbed23
faa54b

Requirements
Must have
• The Sauce name - Drizzle Away!
smaller then name but I would like " BBQ Sauce - Treat your meat to a sweet heat"

award winning ribbon or trophy
Nice to have
• A edgy cartoon pig or cow standing over a vantor style kettle grill using a mop style brush slathering sauce on to a rack of bbq ribs

Dust Off! BBQ in matching front from our logo

```html
<!DOCTYPE html>
<html lang="en">
<head>
<meta charset="utf-8">
<title>Drizzle Away! BBQ Sauce Label</title>
<link rel="stylesheet" href="https://fonts.googleapis.com/css2?family=Arimo:wght@400;700&family=Archivo+Black&display=swap">
<style>
  :root {
    --flame-red: #d21a10;
    --flame-orange: #f37022;
    --flame-yellow: #faa54b;
    --label-red: #eb1f27;
    --deep-red: #c8140f;
    --cream: #f6f0dc;
    --cream-light: #fcf9ce;
    --yellow: #fbed23;
    --maroon: #6b1410;
    --ink: #111111;
    --white: #ffffff;
  }
  * { box-sizing: border-box; margin: 0; padding: 0; }
  html, body { width: 1200px; height: 900px; overflow: hidden; background: var(--white); }
  body { position: relative; font-family: "Arimo", Arial, sans-serif; }

  .label {
    position: absolute; left: 33px; top: 271px; width: 1142px; height: 280px;
    background: linear-gradient(180deg, var(--flame-red) 0%, var(--flame-orange) 50%, var(--flame-red) 100%);
  }
  .flame-border {
    position: absolute; inset: 0;
    background:
      radial-gradient(ellipse 40px 120px at 10px 50%, var(--flame-yellow), transparent 70%),
      radial-gradient(ellipse 40px 120px at 1132px 50%, var(--flame-yellow), transparent 70%),
      linear-gradient(90deg, #2a0a05 0%, transparent 2%, transparent 98%, #2a0a05 100%);
  }

  .side-panel {
    position: absolute; top: 12px; height: 257px;
    background: var(--cream);
  }
  .side-panel.left { left: 32px; width: 880px; }
  .side-panel.right { left: 875px; width: 212px; }

  .usage, .ingredients {
    position: absolute; left: 55px; width: 188px;
    font-weight: 700; font-size: 11.5px; line-height: 15px; color: var(--maroon);
  }
  .usage { top: 27px; }
  .ingredients { top: 74px; }

  .front {
    position: absolute; left: 267px; top: 12px; width: 608px; height: 222px;
    background: radial-gradient(ellipse at 55% 40%, var(--label-red) 0%, var(--deep-red) 100%);
    overflow: hidden;
  }
  .splash {
    position: absolute; border-radius: 50%;
    background: var(--flame-orange); opacity: .85;
  }
  .splash.name { left: 40px; top: 30px; width: 200px; height: 95px; }
  .splash.heat { left: 430px; top: 15px; width: 110px; height: 55px; }

  .ribbon { position: absolute; left: 16px; top: 30px; }

  .brand-name {
    position: absolute; left: 68px; top: 63px; width: 150px;
    font-family: "Archivo Black", "Arial Black", sans-serif;
    font-size: 25px; line-height: 28px; color: var(--ink); text-align: center;
  }
  .product-type {
    position: absolute; left: 58px; top: 150px;
    font-family: "Archivo Black", "Arial Black", sans-serif;
    font-size: 21px; color: var(--yellow); transform: rotate(-14deg);
    letter-spacing: .5px;
  }
  .mascot {
    position: absolute; left: 238px; top: 8px; width: 150px; height: 214px;
    border-radius: 60px 60px 20px 20px;
    background: linear-gradient(180deg, #f2a89c 0%, #c0201c 55%, #9c1410 100%);
    opacity: .9;
  }
  .sweet-heat {
    position: absolute; left: 450px; top: 25px;
    font-family: "Archivo Black", "Arial Black", sans-serif;
    font-size: 13px; color: var(--yellow); transform: rotate(-12deg); line-height: 14px;
  }
  .claims { position: absolute; left: 408px; top: 82px; color: var(--white); }
  .claim-head {
    font-weight: 700; font-size: 19px; line-height: 21px; display: flex; gap: 6px;
  }
  .claim-head svg { flex: none; margin-top: 3px; }
  .claim-note { font-weight: 700; font-size: 9.5px; line-height: 11px; margin: 7px 0 9px 23px; }

  .front-tab {
    position: absolute; left: 474px; top: 226px; width: 200px; height: 26px;
    background: var(--label-red);
    display: flex; align-items: center; justify-content: center;
  }
  .wordmark-text {
    font-weight: 700; font-size: 17px; line-height: 20px; color: var(--white);
    white-space: nowrap;
  }
  .wordmark-text sup { font-size: 8px; vertical-align: 8px; margin-left: 1px; }
  .volume {
    position: absolute; left: 474px; top: 255px; width: 200px; text-align: center;
    font-weight: 700; font-size: 10.5px; line-height: 12px; color: var(--ink);
  }
  .pairings {
    position: absolute; top: 240px;
    font-weight: 700; font-size: 20px; color: var(--maroon);
    display: flex; align-items: center; gap: 6px;
  }
  .pairings.left { left: 272px; }
  .pairings.right { left: 687px; }

  .nutrition {
    position: absolute; left: 902px; top: 18px; width: 186px; color: var(--ink);
    font-size: 10.5px; line-height: 12px;
  }
  .nutrition h2 { text-align: center; font-size: 17px; line-height: 19px; }
  .nutrition .serving { padding-left: 6px; font-size: 11px; }
  .rule-thick { border-top: 5px solid var(--ink); margin: 2px 0; }
  .rule-mid { border-top: 2px solid var(--ink); margin: 1px 0; }
  .row { display: flex; justify-content: space-between; border-bottom: 1px solid var(--ink); padding: 0 2px; font-size: 10px; line-height: 11.5px; }
  .row.bold { font-weight: 700; }
  .row.indent { padding-left: 14px; }
  .row.big { font-size: 13px; line-height: 15px; border: none; }
  .row.plain { border: none; font-size: 9.5px; line-height: 10px; padding-left: 14px; }
</style>
</head>
<body>
  <div class="label">
    <div class="flame-border" role="img" aria-label="Flame border around the label"></div>

    <div class="side-panel left"></div>
    <div class="side-panel right"></div>

    <p class="usage">Excellent for grilling,sautee, marinade and as a dipping sauce.</p>
    <p class="ingredients">Ingredients: tomato concentrate, pineapple juice, water, distilled vinegar, brown sugar,chilli powder spice mix,garlic salt, spice natural flavoring, paprika, mustard seed garlic powder, salt, high fructose corn syrup,corn syrup, onion powder, apple juice, cayenne red peppers, tumeric, ginger, acetic acid, caramel color</p>

    <section class="front">
      <div class="splash name" role="img" aria-label="Orange sauce splash behind the name"></div>
      <div class="splash heat" role="img" aria-label="Orange sauce splash behind the flavour tag"></div>

      <svg class="ribbon" width="52" height="90" viewBox="0 0 52 90" aria-label="Award ribbon">
        <polygon points="14,40 4,84 16,76 24,88 26,44" fill="#f3b71a"/>
        <polygon points="38,40 48,84 36,76 28,88 26,44" fill="#e59a10"/>
        <circle cx="26" cy="26" r="25" fill="#f7c21e"/>
        <circle cx="26" cy="26" r="19" fill="#fcf9ce"/>
      </svg>

      <div class="brand-name">Drizzle Away!</div>
      <div class="product-type">BBQ SAUCE</div>

      <div class="mascot" role="img" aria-label="Cartoon pig chef mascot giving a thumbs up"></div>

      <div class="sweet-heat">Sweet<br>&nbsp;&nbsp;&nbsp;&nbsp;heat</div>

      <div class="claims">
        <div class="claim-head">
          <svg width="16" height="16" viewBox="0 0 16 16"><polygon points="8,0 10,6 16,6 11,10 13,16 8,12 3,16 5,10 0,6 6,6" fill="#fff"/></svg>
          <span>MONUMENTAL<br>FLAVOR!</span>
        </div>
        <p class="claim-note">ALL NATURAL<br>NO HIGH FRUCTOSE CORN SYRUP</p>
        <div class="claim-head">
          <svg width="16" height="16" viewBox="0 0 16 16"><polygon points="8,0 10,6 16,6 11,10 13,16 8,12 3,16 5,10 0,6 6,6" fill="#fff"/></svg>
          <span>GLUTEN FREE</span>
        </div>
        <p class="claim-note">NO PRESERVATIVES<br>NO MSG</p>
      </div>
    </section>

    <div class="front-tab">
      <span class="wordmark-text">DRIZZLE AWAY<sup>TM</sup></span>
    </div>
    <div class="volume">12 FL OZ (355ml)</div>

    <div class="pairings left">PORK
      <svg width="20" height="18" viewBox="0 0 16 16"><polygon points="8,0 10,6 16,6 11,10 13,16 8,12 3,16 5,10 0,6 6,6" fill="#6b1410"/></svg>
      VEGGIES</div>
    <div class="pairings right">FISH
      <svg width="20" height="18" viewBox="0 0 16 16"><polygon points="8,0 10,6 16,6 11,10 13,16 8,12 3,16 5,10 0,6 6,6" fill="#6b1410"/></svg>
      POULTRY</div>

    <section class="nutrition">
      <h2>Nutrition Facts</h2>
      <p class="serving">Serving Size about 2 Tbsp (38g)</p>
      <p class="serving">Serving Per Container: 12</p>
      <div class="rule-thick"></div>
      <div class="row big"><span>Amount Per Serving</span></div>
      <div class="rule-mid"></div>
      <div class="row bold"><span>Calories 50 Calories from 0</span></div>
      <div class="rule-mid"></div>
      <div class="row bold" style="justify-content:flex-end"><span>% Daily Value*</span></div>
      <div class="row bold"><span>Total Fat 0g</span><span>0%</span></div>
      <div class="row indent"><span>Saturated Fat 0g</span><span>0%</span></div>
      <div class="row indent"><span>Trans Fat 0g</span><span></span></div>
      <div class="row bold indent"><span>Cholesterol 0mg</span><span>0%</span></div>
      <div class="row bold indent"><span>Sodium 440mg</span><span>18%</span></div>
      <div class="row bold indent"><span>Total Carbohydrate 13g</span><span>4%</span></div>
      <div class="row indent"><span>Dietary Fiber 0g</span><span>0%</span></div>
      <div class="row indent"><span>Sugars 11g</span><span></span></div>
      <div class="row bold indent" style="font-size:11px"><span>Protein 0g</span><span></span></div>
      <div class="rule-thick"></div>
      <div class="row plain"><span>Vitamin A &nbsp;&lt;2%</span><span>Vitamins &nbsp;&lt;4%</span></div>
      <div class="row plain"><span>Calcium &nbsp;&nbsp;&nbsp;&lt;0%</span><span>Iron &nbsp;&nbsp;&nbsp;&nbsp;&nbsp;&nbsp;2%</span></div>
    </section>
  </div>
</body>
</html>
```